Automotive Accessories Business Card

Design a business template that match our new logo design and our industry.

https://www.kelvramotive.com/

Target Market(s)

Aftermarket auto parts and accessories

Industry/Entity Type

automotive

Contact Information for Business Card

company logo

Font styles to use
Serif
Sans Serif

Colors
EB3D1F
EC4F4E
F09395
F8D3D4
FCEDEE

```html
<!DOCTYPE html>
<html lang="en">
<head>
<meta charset="utf-8">
<title>Kelvra Motive Business Card</title>
<link rel="stylesheet" href="https://fonts.googleapis.com/css2?family=Orbitron:wght@700;800&family=Roboto:wght@400;500;700&display=swap">
<style>
  :root {
    --page: #8f8f8f;
    --red: #d92128;
    --red-light: #e23a40;
    --dark: #3b3b3d;
    --white: #ffffff;
    --text: #333333;
  }
  * { margin: 0; padding: 0; box-sizing: border-box; }
  html, body { width: 1200px; height: 1200px; overflow: hidden; }
  body { background: var(--page); font-family: "Roboto", sans-serif; position: relative; }

  .card { position: absolute; left: 281px; width: 640px; height: 366px; overflow: hidden; }
  .card-front { top: 195px; background: var(--white); }
  .card-back { top: 639px; background: var(--red); }

  .brand { position: absolute; display: flex; align-items: center; gap: 10px;
           font-family: "Orbitron", sans-serif; font-weight: 800; white-space: nowrap; }
  .brand-mark { display: block; background: var(--red); }
  .front-brand { left: 58px; top: 153px; font-size: 22px; color: var(--dark); }
  .front-brand .brand-mark { width: 18px; height: 18px; }

  .contact { position: absolute; left: 363px; top: 72px; color: var(--text); }
  .person-name { font-family: "Orbitron", sans-serif; font-weight: 800; font-size: 24px;
                 color: var(--dark); letter-spacing: -0.5px; line-height: 30px; }
  .person-title { color: var(--red); font-size: 18px; line-height: 22px; margin-bottom: 16px; }
  .contact-row { display: flex; gap: 12px; font-size: 15.5px; line-height: 21.5px; letter-spacing: 0.3px; margin-bottom: 6px; }
  .contact-row svg { flex: none; width: 15px; height: 15px; margin-top: 3px; fill: var(--red); }

  .footer-band { position: absolute; left: 0; bottom: 0; width: 640px; height: 44px; }
  .website { position: absolute; left: 38px; bottom: 13px; color: var(--white);
             font-size: 15px; letter-spacing: 2.2px; }
  .website strong { font-weight: 700; }

  .back-texture { position: absolute; inset: 0;
                  background: radial-gradient(ellipse at 50% 45%, var(--red-light), var(--red) 70%); }
  .back-brand { left: 0; right: 0; top: 148px; justify-content: center; font-size: 40px; color: var(--white); }
  .back-brand .brand-mark { width: 30px; height: 30px; background: var(--white); }
  .services { position: absolute; left: 0; right: 0; top: 289px; text-align: center;
              color: var(--white); font-size: 17px; line-height: 22px; }
</style>
</head>
<body>
  <section class="card card-front">
    <div class="brand front-brand"><span class="brand-mark"></span>KELVRA MOTIVE</div>

    <div class="contact">
      <div class="person-name">DANIEL MOREAU</div>
      <div class="person-title">Founder &amp; CEO</div>
      <div class="contact-row">
        <svg viewBox="0 0 16 16"><path d="M8 0a5.5 5.5 0 0 0-5.5 5.5C2.5 9.5 8 16 8 16s5.5-6.5 5.5-10.5A5.5 5.5 0 0 0 8 0zm0 8a2.5 2.5 0 1 1 0-5 2.5 2.5 0 0 1 0 5z"/></svg>
        <div>250 W. Harbor Ave. Unit B<br>Fontana, CA, 92335<br>United States</div>
      </div>
      <div class="contact-row">
        <svg viewBox="0 0 16 16"><path d="M3.6 1l2.3 2.6-1.3 2c.9 2 2.5 3.7 4.6 4.7l2-1.3L14 11.4 12.5 14C6.6 13.6 2.2 9.2 1.9 3.2z"/></svg>
        <div>1-866-555-0142</div>
      </div>
      <div class="contact-row">
        <svg viewBox="0 0 16 16"><path d="M1 4h14v1L8 9 1 5zm0 2.5l7 4 7-4V13H1z"/></svg>
        <div>sales@kelvramotive.com</div>
      </div>
    </div>

    <svg class="footer-band" viewBox="0 0 640 44" aria-hidden="true">
      <path d="M0 0H270Q290 0 306 13Q322 27 345 28H640V44H0Z" fill="#d92128"/>
      <path d="M312 15H640V26H338Q322 26 312 15Z" fill="#3b3b3d"/>
      <rect x="552" y="15" width="88" height="11" fill="#6a6a6c"/>
    </svg>
    <div class="website">www.<strong>KELVRAMOTIVE</strong>.com</div>
  </section>

  <section class="card card-back">
    <div class="back-texture" role="img" aria-label="Soft red background with a faint perforated texture and vehicle silhouette"></div>
    <div class="brand back-brand"><span class="brand-mark"></span>KELVRA MOTIVE</div>
    <p class="services">Side Step | Side Armor | Hitch | Truck Armor | Off-Road<br>Grilles | Running Boards | Fender Flare | Fender Trim</p>
  </section>
</body>
</html>
```